Beauty Studio Business Card Design

its a new business & I want something different and classy
the strips are part of my decor

Target Market(s)

young girls and mature women

Industry/Entity Type

Business

Contact Information for Business Card

Frae-la-mu 26 0459817362 ABN # all on the front
address on the back + apt times & maybe my name
I would like black & white strips & fancy font with a fancy border around Frae-la-mu

```html
<!DOCTYPE html>
<html lang="en">
<head>
<meta charset="utf-8">
<title>Frae-la-mu Beauty Studio – Business Card</title>
<link href="https://fonts.googleapis.com/css2?family=Arimo:wght@400;700&family=Playfair+Display:wght@400&display=swap" rel="stylesheet">
<style>
  :root {
    --backdrop: #6b6b6b;
    --ink: #000000;
    --paper: #ffffff;
    --ornament-core: #9a9a9a;
    --ornament-edge: #1a1a1a;
    --dots: #555555;
  }
  * { margin: 0; padding: 0; box-sizing: border-box; }
  html, body {
    width: 1200px; height: 900px; overflow: hidden;
    background: var(--backdrop);
    font-family: "Arimo", Arial, sans-serif;
  }
  .card {
    position: absolute; top: 292px;
    width: 540px; height: 316px;
    border-radius: 22px; overflow: hidden;
    background: var(--paper);
  }
  .card--front { left: 40px; }
  .card--back { left: 620px; }
  .stripes {
    position: absolute; left: 0; right: 0;
    background: repeating-linear-gradient(to bottom, var(--ink) 0 4px, var(--paper) 4px 8px);
  }
  /* front */
  .front-top { top: 0; height: 62px; }
  .front-band { position: absolute; top: 62px; left: 0; right: 0; height: 150px; background: var(--ink); }
  .front-bottom { top: 216px; bottom: 0; }
  .ornament {
    position: absolute; left: 170px; width: 140px; border-radius: 50%;
    background: radial-gradient(ellipse at center, var(--ornament-core) 0%, var(--ornament-edge) 70%, rgba(0,0,0,0) 100%);
  }
  .ornament--top { top: 8px; height: 40px; }
  .ornament--bottom { top: 104px; height: 44px; }
  .studio-name {
    position: absolute; top: 46px; left: 60px; width: 360px;
    text-align: center; color: var(--paper);
    font-family: "Playfair Display", Georgia, serif;
    font-size: 44px; font-weight: 400; line-height: 56px;
  }
  .phone-glow {
    position: absolute; left: 100px; top: 256px; width: 270px; height: 26px;
    background: radial-gradient(ellipse at center, var(--paper) 60%, rgba(255,255,255,0) 72%);
  }
  .phone {
    position: absolute; left: 128px; top: 254px;
    font-size: 23px; line-height: 28px; color: var(--ink); letter-spacing: 1px;
  }
  /* back */
  .back-top { top: 0; height: 52px; }
  .back-bottom { top: 232px; bottom: 0; border-top: 6px solid var(--ink); }
  .appointment {
    position: absolute; top: 62px; left: 0; right: 0;
    text-align: center; font-weight: 700; font-size: 16px; color: var(--ink);
  }
  .field-row {
    position: absolute; left: 34px; right: 34px;
    display: flex; align-items: flex-end; gap: 4px;
    font-size: 14px; color: var(--ink);
  }
  .field-row--name { top: 98px; }
  .field-row--date { top: 130px; }
  .field-label { width: 52px; }
  .field-line { flex: 1; border-bottom: 1.5px dotted var(--dots); height: 12px; }
  .field-label--time { width: auto; margin-left: 6px; font-size: 12px; }
  .manager { position: absolute; top: 160px; left: 0; right: 0; text-align: center; color: var(--ink); }
  .manager-name { font-weight: 700; font-size: 14px; }
  .manager-role { font-size: 10px; margin-top: 2px; }
  .address { position: absolute; top: 200px; left: 0; right: 0; text-align: center; font-size: 10px; line-height: 13px; color: var(--ink); }
</style>
</head>
<body>
  <section class="card card--front" aria-label="Card front">
    <div class="stripes front-top"></div>
    <div class="front-band">
      <div class="ornament ornament--top" role="img" aria-label="Fancy ornamental border above the studio name"></div>
      <div class="studio-name">Frae-la-mu</div>
      <div class="ornament ornament--bottom" role="img" aria-label="Fancy ornamental border below the studio name"></div>
    </div>
    <div class="stripes front-bottom"></div>
    <div class="phone-glow"></div>
    <div class="phone">26 0459817362</div>
  </section>

  <section class="card card--back" aria-label="Card back">
    <div class="stripes back-top"></div>
    <div class="appointment">Appointment</div>
    <div class="field-row field-row--name">
      <span class="field-label">Name :</span><span class="field-line"></span>
    </div>
    <div class="field-row field-row--date">
      <span class="field-label">Date :</span><span class="field-line"></span>
      <span class="field-label field-label--time">Time :</span><span class="field-line"></span>
    </div>
    <div class="manager">
      <div class="manager-name">Mara Linden</div>
      <div class="manager-role">Manager</div>
    </div>
    <div class="address">Po Box 418, kellan street<br>Ashford hill, Riverton</div>
    <div class="stripes back-bottom"></div>
  </section>
</body>
</html>
```